Brackenfold Health Web Page

We need a visually exciting webpage that introduces people to our practice. We are a practice that has both physiotherapy and psychology and we need the page to reflect this. We are also split across two practice locations. We need the page to be able to be updated regularly to include a blog spot and the linking in of our facebook page. There should be tabs to introduce our practitioners with some blurbs about them, a tab for people to be able to contact us, a tab to read about physiotherapy services and a tab to talk about psychology services. If there are other tabs than please include these. We are a practice that has treated world class athlete on a regular basis and see our selves as leaders in the field and the website must reflect this. I do not want basic clip-arty type things that anyone could have, we have to have something that draws people in.
Firstly, thanks everyone for their designs. I have attached some links to some physiotherapy websites that I think contain some interesting information and/or layout, as well as some comments,
Hi all,
Reason: Hi Guys,
We are so very close to finding a great design. I feel that we just need a bit of extra time to be able to clinch where we want to be. Thanks for your fantastic designs :)
Regards,
Oliver and Ruth
- 2 Practice Addresses (details to follow for right applications)
Psychology aspect
Physiotherapy aspect
Ability to update blog

```html
<!DOCTYPE html>
<html lang="en">
<head>
<meta charset="utf-8">
<title>Brackenfold Health</title>
<link href="https://fonts.googleapis.com/css2?family=Open+Sans:wght@400;600;700&family=Oswald:wght@400&family=Dancing+Script:wght@600&display=swap" rel="stylesheet">
<style>
:root{
  --brand:#477a92;
  --ink:#333;
  --muted:#666;
  --line:#cfcfcf;
  --accent:#d9434f;
  --alert:#df5a64;
  --band:#eeeeee;
  --card:#fff;
  --bar:#6b6b6b;
  --foot:#323232;
  --foot-deep:#232323;
  --foot-text:#9a9a9a;
  --btn-dark:#2f5566;
}
*{box-sizing:border-box;margin:0;padding:0}
html,body{width:753px;height:1200px;overflow:hidden}
body{position:relative;font-family:"Open Sans",Arial,sans-serif;color:var(--ink);background:#fff}
.abs{position:absolute}

.topbar{left:0;top:0;width:753px;height:20px;font-size:6.5px;color:#777;line-height:20px}
.topbar .left{left:103px}
.topbar .right{right:103px;color:#555}
.topbar b{font-weight:700}

.header{left:0;top:20px;width:753px;height:93px;background:var(--brand)}
.logo{left:104px;top:14px;color:#fff;font-weight:700;font-size:13px;letter-spacing:.5px}
.social{left:500px;top:13px;display:flex;gap:4.5px}
.social span{width:21px;height:21px;border-radius:50%;background:#fff;display:block}

.nav{left:103px;top:78px;width:547px;height:35px;background:#fff;border-radius:3px 3px 0 0;display:flex;font-size:7.6px;border-bottom:2px solid #e4e4e4}
.nav a{display:block;padding:0 6px;line-height:34px;border-right:1px solid #e6e6e6;text-decoration:none;color:#888}
.nav a.on{color:#333}
.nav a.sched{line-height:1;padding-top:12px}
.nav a.sched small{display:block;font-size:3.5px;margin-top:1px}
.nav .search{margin-left:auto;padding-right:14px;line-height:34px;color:#aaa;font-size:6.8px}

.hero{left:0;top:113px;width:753px;height:179px;background:linear-gradient(90deg,#e9eef7 0%,#f6f8fc 50%,#ecf0f8 100%)}
.hero-photo{left:72px;top:0;width:272px;height:179px;background:radial-gradient(ellipse at 50% 55%,#f1ddca 0%,#e8edf4 60%,rgba(233,238,247,0) 75%)}
.tagline{left:366px;top:36px;font-family:"Dancing Script",cursive;font-size:28px;color:#3b3b3b}
.tag-rule{left:470px;top:72px}
.hero-label{font-family:"Oswald",sans-serif;font-size:10px;color:#fff;background:#777;padding:0 3px;line-height:13px}

.callband{left:0;top:292px;width:753px;height:64px;background:var(--band);border-top:1px solid #e2e2e2;border-bottom:1px solid #e2e2e2}
.callbar{left:112px;top:17px;width:530px;height:28px;background:var(--alert);border-radius:3px;border-bottom:2px solid #c0424c;color:#fff;font-size:9.6px;line-height:27px;text-align:center;letter-spacing:.2px}

.card{top:382px;width:166px;height:146px;background:var(--card);border:1px solid #ddd;border-radius:3px;box-shadow:0 2px 0 #d5d5d5;text-align:center}
.card svg{margin-top:11px}
.card h3{font-weight:400;font-size:9.4px;margin-top:9px;color:#222}
.card p{font-size:7.1px;line-height:11.2px;color:#444;margin:6px 10px 0}
.card .more{display:inline-block;margin-top:7px;font-size:6.6px;font-weight:700;border:1px solid #bbb;border-radius:2px;padding:1px 6px;background:#fff;color:#333}
.card .more.dark{background:var(--btn-dark);color:#fff;border-color:var(--btn-dark)}

.newsband{left:0;top:554px;width:753px;height:222px;background:var(--band);border-top:1px solid #e0e0e0;border-bottom:1px solid #e0e0e0}
.sec-title{font-size:9.2px;color:#333;letter-spacing:.3px}
.sec-rule{height:2px;background:#d0d0d0}
.sec-rule::before{content:"";display:block;width:56px;height:2px;background:var(--accent)}
.post h4{font-weight:400;font-size:10.4px;color:#222}
.post .date{font-size:6.4px;color:#888;margin-top:5px}
.post .img{width:146px;height:89px;margin-top:3px}
.post .read{display:inline-block;margin-top:9px;background:#666;color:#fff;font-size:6.4px;padding:3px 6px;border-radius:2px;border-bottom:2px solid #444}
.pager{left:380px;top:744px;display:flex;align-items:center;gap:3px}
.pager i{width:4px;height:4px;border-radius:50%;background:#555;display:block}
.pager i.off{background:#bbb}
.pager b{width:13px;height:13px;background:#ccc;border:1px solid #bbb;display:block;margin-left:5px}
.pager b+b{margin-left:2px}

.hl-bar{left:470px;width:176px;height:20px;background:var(--bar);color:#fff;font-size:8px;line-height:19px;padding-left:5px;border-bottom:2px solid #4e4e4e;border-radius:2px}
.hl-bar.open{background:#585858}
.hl-bar::after{content:"+";position:absolute;right:5px;top:5px;width:9px;height:9px;background:#999;color:#555;font-size:8px;line-height:8px;text-align:center}
.hl-text{left:476px;top:620px;width:166px;font-size:7.1px;line-height:11.2px;color:#444}

.docs{left:126px;top:820px;display:flex;gap:14px}
.docs div{width:90px;height:89px}
.arrow{width:13px;height:13px;background:#ddd;border:1px solid #bbb;top:858px}

.footer{left:0;top:920px;width:753px;height:188px;background:var(--foot)}
.fcol{top:20px;width:131px}
.fcol h5{font-weight:400;font-size:9px;color:var(--foot-text);letter-spacing:.3px}
.fcol .rule{height:1px;background:#777;margin-top:5px}
.fcol .rule::before{content:"";display:block;width:66px;height:2px;background:var(--accent)}
.fcol ul{list-style:none;margin-top:7px}
.fcol li{font-size:7.1px;color:var(--foot-text);line-height:17.4px;border-bottom:1px solid #3c3c3c;white-space:nowrap}
.fcol.links li{border:none;padding-left:10px;position:relative;line-height:19.5px}
.fcol.links li::before{content:"";position:absolute;left:2px;top:9px;width:3px;height:3px;border-radius:50%;background:#888}
.sponsor{background:#4a4a4a;border-radius:3px}
.contact{display:flex;align-items:center;gap:7px;font-size:7.1px;color:var(--foot-text);height:24px;white-space:nowrap}
.contact i{width:13px;height:13px;border-radius:50%;background:#777;display:flex;align-items:center;justify-content:center;flex:none}
.appt{display:inline-block;margin-top:4px;background:#fff;color:#333;font-size:6.8px;font-weight:600;padding:3px 8px 3px 18px;border-radius:2px;position:relative}

.bottom{left:0;top:1108px;width:753px;height:92px;background:var(--foot-deep);text-align:center;color:#aaa;font-size:6.6px}
.bottom p{position:absolute;left:0;width:753px}
.bottom .dots{display:flex;justify-content:center;gap:4px}
.bottom .dots span{width:11px;height:11px;border-radius:50%;background:#777;display:block}
.totop{left:632px;top:15px}
</style>
</head>
<body>

<div class="abs topbar">
  <span class="abs left">Wednesday, 15 January 2014 &nbsp;&nbsp; Our Practitioners &nbsp;|&nbsp; Clinic Blog &nbsp;|&nbsp; Latest News</span>
  <span class="abs right"><b>Northside:</b> 555.301.8824 | <b>Southside:</b> 555.301.9910</span>
</div>

<header class="abs header">
  <div class="abs logo">BRACKENFOLD</div>
  <div class="abs social" aria-label="Social links">
    <span></span><span></span><span></span><span></span><span></span><span></span>
  </div>
</header>

<nav class="abs nav">
  <a class="on">Home</a><a>Practitioners</a><a>About us</a><a>Physiotherapy</a><a>Psychology</a>
  <a class="sched">Book<small>an appointment</small></a>
  <a>Blog</a><a>Locations</a><a>Contacts</a>
  <span class="search">&#9906; search...</span>
</nav>

<section class="abs hero">
  <div class="abs hero-photo" role="img" aria-label="Photo of a smiling woman with arms raised against a bright sky"></div>
  <div class="abs tagline">Move well, feel well</div>
  <svg class="abs tag-rule" width="110" height="8" viewBox="0 0 110 8"><path d="M2 5 Q55 1 107 6" stroke="#444" stroke-width="1.3" fill="none"/></svg>
  <div class="abs" style="left:386px;top:89px"><span class="hero-label">Physiotherapy trusted by world class athletes</span></div>
  <div class="abs" style="left:386px;top:108px"><span class="hero-label">Psychology for mind and performance</span></div>
</section>

<section class="abs callband">
  <div class="abs callbar">&#9990;&nbsp; Bookings: 555.301.4410 &nbsp;&nbsp; | &nbsp;&nbsp; Northside Clinic: 555.301.8824 &nbsp;&nbsp; | &nbsp;&nbsp; Southside Clinic: 555.301.9910</div>
</section>

<article class="abs card" style="left:115px">
  <svg width="30" height="30" viewBox="0 0 30 30"><circle cx="15" cy="4.5" r="3.2" fill="#111"/><path d="M15 9v10M6 12l9 2 9-2M15 19l-6 9M15 19l6 9" stroke="#111" stroke-width="2.6" fill="none" stroke-linecap="round"/></svg>
  <h3>Physiotherapy</h3>
  <p>Sports injury care, rehabilitation and movement programs from physios who treat elite athletes every season, tailored to your goals.</p>
  <span class="more">More</span>
</article>
<article class="abs card" style="left:290px">
  <svg width="30" height="30" viewBox="0 0 30 30"><path d="M8 27v-6C4 19 3 15 3 12 3 6 8 2 14 2s11 4 11 10l3 5h-3v4a3 3 0 0 1-3 3h-3v3" fill="none" stroke="#111" stroke-width="2.4" stroke-linejoin="round"/></svg>
  <h3>Psychology</h3>
  <p>Confidential support for stress, anxiety and recovery, plus performance coaching that helps athletes and everyday clients thrive.</p>
  <span class="more">More</span>
</article>
<article class="abs card" style="left:466px">
  <svg width="34" height="30" viewBox="0 0 34 30"><path d="M9 2a6 6 0 0 1 6 6c0 5-6 11-6 11S3 13 3 8a6 6 0 0 1 6-6z" fill="#111"/><circle cx="9" cy="8" r="2.2" fill="#fff"/><path d="M25 9a6 6 0 0 1 6 6c0 5-6 11-6 11s-6-6-6-11a6 6 0 0 1 6-6z" fill="#111"/><circle cx="25" cy="15" r="2.2" fill="#fff"/></svg>
  <h3>Two Practice Locations</h3>
  <p>Visit us at our Northside or Southside clinic, both with full physiotherapy and psychology teams and easy online booking.</p>
  <span class="more dark">More</span>
</article>

<section class="abs newsband">
  <div class="abs sec-title" style="left:106px;top:9px">FROM OUR BLOG</div>
  <div class="abs sec-rule" style="left:106px;top:23px;width:358px"></div>
  <div class="abs sec-title" style="left:470px;top:9px">HIGHLIGHTS</div>
  <div class="abs sec-rule" style="left:470px;top:23px;width:176px"></div>

  <div class="abs post" style="left:111px;top:37px">
    <h4>Back from a knee injury</h4>
    <div class="date">&#9638; 13 March 2012</div>
    <div class="img" role="img" aria-label="Photo of a physiotherapy rehabilitation session" style="background:linear-gradient(160deg,#8a8f86,#3f4a3d 60%,#c9c9c4)"></div>
    <span class="read">Read More &#8853;</span>
  </div>
  <div class="abs post" style="left:291px;top:37px">
    <h4>Calm before the race</h4>
    <div class="date">&#9638; 15 March 2012</div>
    <div class="img" role="img" aria-label="Photo illustrating a psychology blog post" style="background:linear-gradient(150deg,#f3f3f5,#b9c4cf 45%,#d98a7a 70%,#f2f2f2)"></div>
    <span class="read">Read More &#8853;</span>
  </div>
</section>

<div class="abs pager"><i></i><i class="off"></i><i></i><b></b><b></b></div>

<div class="abs hl-bar open" style="top:590px">Elite athlete rehabilitation</div>
<p class="abs hl-text">Our physios have guided national and world class athletes back to competition, using the same proven methods for every client.</p>
<div class="abs hl-bar" style="top:669px">Sports injury assessment</div>
<div class="abs hl-bar" style="top:694px">Performance psychology</div>
<div class="abs hl-bar" style="top:719px">Leaders in the field since 2001</div>
<div class="abs hl-bar" style="top:744px">Follow us on Facebook</div>

<div class="abs sec-title" style="left:106px;top:793px">MEET OUR PRACTITIONERS</div>
<div class="abs sec-rule" style="left:106px;top:808px;width:540px"></div>
<div class="abs arrow" style="left:107px"></div>
<div class="abs arrow" style="left:634px"></div>
<div class="abs docs">
  <div role="img" aria-label="Portrait of a physiotherapist" style="background:linear-gradient(180deg,#c9a24c,#b98a64 50%,#e7e3dc)"></div>
  <div role="img" aria-label="Portrait of a physiotherapist" style="background:linear-gradient(180deg,#8a6a4c,#d3a382 50%,#eeeeee)"></div>
  <div role="img" aria-label="Portrait of a psychologist" style="background:linear-gradient(180deg,#c0a06b,#e0b795 50%,#f0f0f0)"></div>
  <div role="img" aria-label="Portrait of a psychologist" style="background:linear-gradient(180deg,#b84848,#5a3b2c 50%,#e8e8e8)"></div>
  <div role="img" aria-label="Portrait of a physiotherapist" style="background:linear-gradient(180deg,#c7c2b4,#b0805e 50%,#efefef)"></div>
</div>

<footer class="abs footer">
  <div class="abs fcol" style="left:106px">
    <h5>LATEST POSTS</h5><div class="rule"></div>
    <ul><li>Back from a knee injury</li><li>Calm before the race</li><li>Desk posture basics</li><li>Sleep and recovery</li><li>Running without pain</li><li>Managing exam stress</li></ul>
  </div>
  <div class="abs fcol links" style="left:242px">
    <h5>USEFUL LINKS</h5><div class="rule"></div>
    <ul><li>Our Practitioners</li><li>Physiotherapy Services</li><li>Psychology Services</li><li>Health Insurances</li><li>Clinic Blog</li><li>Facebook Page</li></ul>
  </div>
  <div class="abs fcol" style="left:379px">
    <h5>OUR PARTNERS</h5><div class="rule"></div>
    <div class="abs sponsor" style="left:12px;top:50px;width:92px;height:28px"></div>
    <div class="abs sponsor" style="left:20px;top:95px;width:76px;height:24px"></div>
    <div class="abs sponsor" style="left:16px;top:138px;width:86px;height:22px"></div>
  </div>
  <div class="abs fcol" style="left:516px">
    <h5>CONTACTS</h5><div class="rule"></div>
    <div style="margin-top:4px">
      <div class="contact"><i><svg width="7" height="7" viewBox="0 0 10 10"><path d="M5 1L1 5h2v4h4V5h2z" fill="#fff"/></svg></i>Northside: Harlow Bay, 4th Av</div>
      <div class="contact"><i><svg width="7" height="7" viewBox="0 0 10 10"><path d="M5 1L1 5h2v4h4V5h2z" fill="#fff"/></svg></i>Southside: Elm Quay, 12 Rowe St</div>
      <div class="contact"><i><svg width="7" height="7" viewBox="0 0 10 10"><path d="M2 1l2 2-1 1.5a6 6 0 0 0 2.5 2.5L7 6l2 2-1.5 1.5C4 9 1 6 .5 2.5z" fill="#fff"/></svg></i>Northside: +555.301.8824</div>
      <div class="contact"><i><svg width="7" height="7" viewBox="0 0 10 10"><path d="M2 1l2 2-1 1.5a6 6 0 0 0 2.5 2.5L7 6l2 2-1.5 1.5C4 9 1 6 .5 2.5z" fill="#fff"/></svg></i>Southside: +555.301.9910</div>
      <span class="appt"><svg class="abs" style="left:6px;top:3px" width="7" height="7" viewBox="0 0 10 10"><path d="M1 5l3 3 5-6" stroke="#555" stroke-width="1.6" fill="none"/></svg>Request an appointment</span>
    </div>
  </div>
</footer>

<section class="abs bottom">
  <p style="top:19px">Our Practitioners &nbsp;|&nbsp; Clinic Blog &nbsp;|&nbsp; Latest News</p>
  <p style="top:30px">Built with HTML5 and CSS3</p>
  <p style="top:41px">Copyright © 2013 Brackenfold Health™</p>
  <div class="abs dots" style="left:0;width:753px;top:53px"><span></span><span></span><span></span><span></span><span></span></div>
  <p style="top:66px">Powered by Fenwick Theme Framework</p>
  <svg class="abs totop" width="8" height="6" viewBox="0 0 8 6"><path d="M1 5l3-3 3 3" stroke="#aaa" stroke-width="1.3" fill="none"/></svg>
</section>

</body>
</html>
```